TIMBER DECK COMPANY FLYER

We need a flyer design for a Timber Decking company, we specialise in timber decks, stairs, privacy screens, maintenance and pergolas. I have attatched some pictures which you can incorporate if you think they need cropping go for it. We offer amazing decks at affordable prices by qualified tradespeople.
My logo is a dull green I would like this to be changed to a more lime bright green please. Also my logo is too big I would like this logo halved in size please. And the colours in the brochure maybe a blackbackground with lime green and other colours you think will work. We will also beat any reputable Decking companies quote by 10%. Our decks add style, class, longjevity and practicality to any home. The final design should be modern and cutting edge.

Target Market(s)

home owners

Industry/Entity Type

It Company

Logo Text

CRISP PLANKWORKS GROUP

Requirements
Must have
• DECKS
STAIRS
PERGOLAS
PRIVACY SCREENS
DECK MAINTENANCE

CONTACT-GORDON-0438261507

MUST HAVE LIKE US ON PAGEBOARD LOGO

www.crispplankworksgroup.com.au
Nice to have
• Please let me know if need more photos etc

```html
<!DOCTYPE html>
<html lang="en">
<head>
<meta charset="utf-8">
<title>Crisp Plankworks Group – Flyer</title>
<link rel="stylesheet" href="https://fonts.googleapis.com/css2?family=Anton&family=Black+Ops+One&family=Lato:wght@400;700;900&display=swap">
<style>
  :root {
    --page-bg: #8c8c8c;
    --lime: #8cc63f;
    --lime-bright: #a6d83a;
    --mint: #e4f2c8;
    --mint-light: #f4faea;
    --wood-dark: #4a2414;
    --wood: #7a3d1f;
    --wood-light: #a65a2c;
    --bubble: #4f7d1e;
    --bubble-edge: #e8f5c8;
    --offer-yellow: #f6d21c;
    --offer-green: #d6ef5a;
    --ink: #1d1d1d;
    --accent-red: #8a2a12;
    --button: #f7c64a;
    --button-edge: #e39a1d;
    --white: #ffffff;
  }
  * { box-sizing: border-box; margin: 0; padding: 0; }
  html, body { width: 1200px; height: 774px; overflow: hidden; background: var(--page-bg); }
  body { position: relative; font-family: "Lato", sans-serif; }

  .flyer {
    position: absolute; left: 320px; top: 27px; width: 560px; height: 720px;
    background: linear-gradient(180deg, var(--mint-light) 0%, var(--mint) 60%, #d5eaa8 100%);
    overflow: hidden; box-shadow: 0 4px 14px rgba(0,0,0,.35);
  }
  .flyer__waves { position: absolute; inset: 0; }

  .hero {
    position: absolute; left: 14px; top: 0; width: 546px; height: 300px;
    border: 6px solid var(--lime); border-top: 0; border-right: 0;
    border-bottom-left-radius: 70px; overflow: hidden;
    background: linear-gradient(180deg, #cfd8c8 0%, #6f8a52 22%, #6a2e18 34%, #5b2614 60%, #7a3a1c 100%);
  }
  .hero::after {
    content: ""; position: absolute; inset: 0;
    background: repeating-linear-gradient(100deg, rgba(0,0,0,.08) 0 3px, transparent 3px 26px);
  }

  .logo-tab {
    position: absolute; left: 22px; top: 0; width: 292px; height: 86px;
    background: var(--white); border-bottom-right-radius: 34px;
    display: flex; align-items: center; gap: 14px; padding-left: 22px; z-index: 3;
    box-shadow: 2px 2px 0 var(--lime);
  }
  .logo-tab__mark { width: 16px; height: 16px; background: var(--lime-bright); flex: none; }
  .logo-tab__name {
    font-family: "Lato", sans-serif; font-weight: 700; font-size: 14px;
    line-height: 1.25; color: var(--ink); letter-spacing: .3px;
  }

  .headline {
    position: absolute; left: 40px; top: 148px; width: 420px; z-index: 3;
    font-family: "Anton", sans-serif; font-size: 30px; line-height: 1.05;
    color: var(--white); text-align: center; text-shadow: 2px 2px 3px rgba(0,0,0,.7);
  }

  .offer-bubble { position: absolute; left: 300px; top: 258px; width: 250px; height: 170px; z-index: 4; }
  .offer-bubble__text {
    position: absolute; left: 318px; top: 282px; width: 214px; z-index: 5; text-align: center;
    font-family: "Black Ops One", sans-serif; line-height: 1.2;
  }
  .offer-bubble__title { color: var(--offer-yellow); font-size: 24px; display: block; }
  .offer-bubble__body { color: var(--offer-green); font-size: 13px; display: block; margin-top: 4px; }

  .gallery {
    position: absolute; left: 28px; top: 354px; width: 532px; height: 238px;
    background: linear-gradient(90deg, var(--wood-dark), var(--wood) 50%, var(--wood-dark));
  }
  .gallery__photo { position: absolute; border: 2px solid var(--mint-light); }
  .photo--plunge { left: 6px; top: 8px; width: 138px; height: 104px;
    background: linear-gradient(160deg, #7a6a55, #2d3a3a 45%, #6a3a20); }
  .photo--deck { left: 6px; top: 120px; width: 138px; height: 110px;
    background: linear-gradient(170deg, #d8d8d0 0%, #6a6a60 35%, #8a3e1a 60%, #b25a28 100%); }
  .photo--pool { left: 152px; top: 8px; width: 170px; height: 222px;
    background: linear-gradient(180deg, #b8c4b0 0%, #3c5a2c 40%, #4c8ab0 70%, #9a5a30 100%); }
  .photo--stairs { left: 330px; top: 8px; width: 196px; height: 222px;
    background: linear-gradient(120deg, #2f4a22 0%, #3e6a2c 45%, #c9a878 75%, #e4cfa4 100%); }

  .promise {
    position: absolute; left: 28px; top: 604px; width: 532px; text-align: center;
    font-weight: 900; font-size: 14.5px; line-height: 1.35; color: var(--ink);
  }
  .promise__figure { color: var(--accent-red); font-size: 17px; }

  .footer { position: absolute; left: 0; top: 648px; width: 560px; height: 72px; }
  .footer__band { position: absolute; inset: 0; }
  .services {
    position: absolute; left: 16px; top: 6px; list-style: none;
    font-size: 11px; line-height: 1.18; color: var(--white); text-transform: uppercase;
  }
  .contact {
    position: absolute; left: 168px; top: 4px; width: 130px; text-align: center; color: var(--white);
  }
  .contact__label { font-size: 14px; font-weight: 400; display: block; }
  .contact__name { font-size: 18px; font-weight: 900; display: block; line-height: 1.1; }
  .contact__phone { font-size: 20px; font-weight: 900; display: block; line-height: 1.15; }

  .follow-button {
    position: absolute; left: 338px; top: 6px; width: 180px; height: 36px;
    background: linear-gradient(180deg, #fde39a, var(--button));
    border: 2px solid var(--button-edge); border-radius: 8px;
    display: flex; align-items: center; justify-content: center; gap: 8px;
    font-weight: 900; font-size: 15px; color: var(--ink);
  }
  .follow-button__mark { width: 18px; height: 18px; background: #3b5998; border-radius: 3px; flex: none; }
  .website {
    position: absolute; right: 14px; bottom: 6px;
    font-weight: 900; font-size: 12.5px; color: var(--ink);
  }
</style>
</head>
<body>
<main class="flyer">
  <svg class="flyer__waves" width="560" height="720" viewBox="0 0 560 720" aria-hidden="true">
    <path d="M0 330 C140 300 260 380 560 330" fill="none" stroke="#fff" stroke-opacity=".55" stroke-width="3"/>
    <path d="M0 600 C160 570 300 640 560 590" fill="none" stroke="#fff" stroke-opacity=".5" stroke-width="3"/>
    <path d="M0 40 C10 200 4 280 14 330" fill="none" stroke="var(--lime)" stroke-width="10"/>
  </svg>

  <div class="hero" role="img" aria-label="Photo of a timber deck beside a pool with a shed and garden behind"></div>

  <div class="logo-tab">
    <span class="logo-tab__mark"></span>
    <span class="logo-tab__name">CRISP PLANKWORKS<br>GROUP</span>
  </div>

  <h1 class="headline">we specialise in<br>timber decks, stairs, privacy<br>screens, maintenance and<br>pergolas.</h1>

  <svg class="offer-bubble" viewBox="0 0 250 170" aria-hidden="true">
    <path d="M60 140 L30 168 L90 150 Z" fill="var(--bubble)" stroke="var(--bubble-edge)" stroke-width="3"/>
    <ellipse cx="125" cy="80" rx="118" ry="72" fill="var(--bubble)" stroke="var(--bubble-edge)" stroke-width="4"/>
  </svg>
  <p class="offer-bubble__text">
    <span class="offer-bubble__title">WE OFFER</span>
    <span class="offer-bubble__body">AMAZING DECKS AT<br>AFFORDABLE<br>PRICES BY QUALIFIED<br>TRADESPEOPLE.</span>
  </p>

  <section class="gallery">
    <div class="gallery__photo photo--plunge" role="img" aria-label="Photo of a plunge pool framed by timber decking"></div>
    <div class="gallery__photo photo--deck" role="img" aria-label="Photo of a freshly laid timber deck beside a house"></div>
    <div class="gallery__photo photo--pool" role="img" aria-label="Photo of a pool with timber surround and glass fence among trees"></div>
    <div class="gallery__photo photo--stairs" role="img" aria-label="Photo of timber stairs beside leafy garden plants"></div>
  </section>

  <p class="promise">We will also beat any reputable Decking companies quote by <span class="promise__figure">10%.</span><br>Ourdecks add style, class, longjevity and practicality to any home.</p>

  <footer class="footer">
    <svg class="footer__band" width="560" height="72" viewBox="0 0 560 72" aria-hidden="true">
      <defs>
        <linearGradient id="woodBand" x1="0" x2="1">
          <stop offset="0" stop-color="var(--wood-dark)"/>
          <stop offset="1" stop-color="var(--wood-light)"/>
        </linearGradient>
      </defs>
      <path d="M0 0 H290 L330 46 H560 V72 H0 Z" fill="url(#woodBand)"/>
    </svg>
    <ul class="services">
      <li>Decks</li><li>Stairs</li><li>Pergolas</li><li>Privacy Screens</li><li>Deck Maintenance</li>
    </ul>
    <p class="contact">
      <span class="contact__label">CONTACT-</span>
      <span class="contact__name">GORDON</span>
      <span class="contact__phone">0438261507</span>
    </p>
    <div class="follow-button">Follow us PAGEBOARD</div>
    <p class="website">www.crispplankworksgroup.com.au</p>
  </footer>
</main>
</body>
</html>
```